Letterhead and Envelope Only (no biz card)
Leadership Development & Coaching Start Up
I also really like it when the swirls are not perfectly positioned on the page...bleeding off the page looks good. Thanks everyone!
Thanks for submitting your designs! Something else to keep in mind, I am rather feminine...I prefer softer lines and fainter watermarks in the background. I also really prefer the contact info to be on the bottom of the design.
Correction, I like the contact info on the bottom in #1 (not #3.)
My logo designer is out of the country, I should have those files for you in the next couple of days.
From the three designs so far, I like the swirls in #2. I like the contact info on the bottom in #3.
If possible, I'd like to have 2 letterhead designs in my winner...so I can use both for various purposes.
could you please upload the ai or eps file of logo?

```html
<!DOCTYPE html>
<html lang="en">
<head>
<meta charset="UTF-8">
<title>Velmora Stationery — Letterhead and Envelope</title>
<link href="https://fonts.googleapis.com/css2?family=Roboto:wght@400;700&display=swap" rel="stylesheet">
<style>
  :root {
    --brand-blue: #1d3d8c;
    --brand-gold: #f6b21a;
    --gold-deep: #eea20c;
    --watermark: #fbefd6;
    --paper: #ffffff;
    --page-edge: #c9c9c9;
    --window-edge: #b9b9b9;
    --window-fill: #f4f4f4;
    --canvas: #ffffff;
  }
  * { box-sizing: border-box; margin: 0; padding: 0; }
  html, body {
    width: 1200px; height: 737px; overflow: hidden;
    background: var(--canvas);
    font-family: "Roboto", Arial, sans-serif;
  }
  .sheet {
    position: absolute;
    background: var(--paper);
    border: 1px solid var(--page-edge);
    overflow: hidden;
  }
  .letterhead { left: 29px; top: 7px; width: 530px; height: 706px; }
  .envelope-front { left: 581px; top: 12px; width: 595px; height: 550px; }

  .brand {
    position: absolute;
    display: flex; align-items: center; gap: 8px;
  }
  .brand-name {
    font-weight: 700; font-size: 36px; line-height: 1;
    color: var(--brand-blue); letter-spacing: 0.5px;
  }
  .brand-dot {
    width: 26px; height: 26px; border-radius: 50%;
    background: var(--brand-gold);
  }
  .brand-tagline {
    position: absolute;
    font-size: 6px; font-weight: 700; color: var(--brand-gold);
    text-transform: uppercase; letter-spacing: 0.4px;
  }
  .letterhead .brand { left: 104px; top: 42px; }
  .letterhead .brand-tagline { left: 190px; top: 82px; }
  .envelope-front .brand { left: 16px; top: 16px; }
  .envelope-front .brand-name { font-size: 30px; }
  .envelope-front .brand-dot { width: 22px; height: 22px; }
  .envelope-front .brand-tagline { left: 84px; top: 50px; }

  .watermark {
    position: absolute;
    background: radial-gradient(ellipse at 50% 55%, var(--watermark) 0%, var(--watermark) 45%, rgba(251,239,214,0) 72%);
  }
  .letterhead .watermark { left: 30px; top: 210px; width: 440px; height: 460px; }
  .envelope-front .watermark { left: 370px; top: 10px; width: 230px; height: 230px; }

  .address-window {
    position: absolute; left: 74px; top: 106px; width: 238px; height: 98px;
    border: 1px solid var(--window-edge); border-radius: 10px;
    background: var(--window-fill);
  }

  .contact-band { position: absolute; left: 0; width: 100%; }
  .contact-band svg { display: block; width: 100%; height: 100%; }
  .contact-line {
    position: absolute; left: 0; right: 0;
    font-size: 8px; color: var(--brand-blue); text-align: center;
  }
  .letterhead .contact-band { bottom: 0; height: 42px; }
  .letterhead .contact-line { bottom: 10px; }
  .envelope-front .contact-band { top: 230px; height: 40px; }
  .envelope-front .contact-line { top: 14px; left: 40px; text-align: left; }

  .envelope-flap { position: absolute; left: 590px; top: 305px; width: 586px; height: 165px; }
</style>
</head>
<body>

<section class="sheet letterhead" aria-label="Letterhead">
  <div class="watermark" role="img" aria-label="Faint palm and swirl watermark"></div>
  <div class="brand">
    <span class="brand-name">velmora</span>
    <span class="brand-dot"></span>
  </div>
  <span class="brand-tagline">Leadership &amp; Coaching</span>
  <div class="contact-band">
    <svg viewBox="0 0 530 42" preserveAspectRatio="none">
      <rect x="0" y="8" width="530" height="34" fill="var(--brand-gold)"/>
      <path d="M440 42 C470 22 500 12 530 8 L530 42 Z" fill="var(--brand-blue)"/>
    </svg>
    <p class="contact-line">2140 Linden Crest Way, Alder, CO 80412 | Phone: 555.014.2290 | www.velmoragroup.com</p>
  </div>
</section>

<section class="sheet envelope-front" aria-label="Envelope front">
  <div class="watermark" role="img" aria-label="Faint swirl watermark"></div>
  <div class="brand">
    <span class="brand-name">velmora</span>
    <span class="brand-dot"></span>
  </div>
  <span class="brand-tagline">Leadership &amp; Coaching</span>
  <div class="address-window"></div>
  <div class="contact-band">
    <svg viewBox="0 0 595 40" preserveAspectRatio="none">
      <rect x="0" y="0" width="595" height="40" fill="var(--brand-gold)"/>
      <path d="M0 0 L595 0 L595 2 L0 2 Z" fill="var(--brand-gold)"/>
      <path d="M520 0 L595 0 L595 36 C575 20 550 8 520 0 Z" fill="var(--brand-blue)"/>
    </svg>
    <p class="contact-line">2140 Linden Crest Way, Alder, CO 80412 | Phone: 555.014.2290 | www.velmoragroup.com</p>
  </div>
</section>

<svg class="envelope-flap" viewBox="0 0 586 165" aria-label="Envelope back flap">
  <path d="M0 0 L586 0 L586 128 C586 146 578 152 560 154 C420 162 170 162 30 154 C10 152 2 144 0 126 Z" fill="var(--brand-gold)"/>
  <path d="M18 20 L568 20 L560 96 C556 118 548 124 530 126 C400 134 190 134 60 126 C40 124 32 118 28 100 Z" fill="var(--gold-deep)"/>
</svg>

</body>
</html>
```